Business Cards for a small business advisory (business services)

Professional look. Same as would apply for a lawyer, accountant, or other financial services professional. Please use the logo colors

Target Market(s)

small business owners

Industry/Entity Type

Financial Servics

Contact Information for Business Card

Name: Gavin L. Whitmore, CAIA / Title: Business Advisor / Office #: (718) 294-7716 / Mobile #: (917) 382-5047 / Email: g.whitmore@clearfieldventurepartners.example / Web: www.clearfieldventurepartners.example

Font styles to use
Sans Serif

```html
<!DOCTYPE html>
<html lang="en">
<head>
<meta charset="utf-8">
<title>Clearfield Venture Partners – Business Cards</title>
<link href="https://fonts.googleapis.com/css2?family=Montserrat:wght@400;500;600;700;800&display=swap" rel="stylesheet">
<style>
  :root {
    --navy: #1c3a6e;
    --green: #8cc63f;
    --white: #ffffff;
    --stage: #e9ebee;
  }
  * { margin: 0; padding: 0; box-sizing: border-box; }
  html, body { width: 1200px; height: 900px; overflow: hidden; }
  body {
    background: var(--stage);
    font-family: "Montserrat", sans-serif;
    display: flex;
    flex-direction: column;
    align-items: center;
    justify-content: center;
    gap: 40px;
  }
  .card {
    position: relative;
    width: 720px;
    height: 410px;
    border-radius: 22px;
    overflow: hidden;
    box-shadow: 0 6px 18px rgba(20, 30, 50, 0.18);
  }

  /* Back */
  .card-back { background: var(--navy); }
  .card-back .brand {
    position: absolute;
    left: 0; right: 0; top: 150px;
    text-align: center;
  }
  .brand-row { display: inline-flex; align-items: center; gap: 16px; }
  .brand-dot {
    width: 30px; height: 30px; border-radius: 50%;
    background: var(--green);
    flex: none;
  }
  .brand-name {
    font-weight: 700;
    font-size: 40px;
    letter-spacing: 0.5px;
    color: var(--white);
    white-space: nowrap;
  }
  .brand-tagline {
    margin-top: 12px;
    font-size: 11px;
    font-weight: 600;
    letter-spacing: 1.2px;
    text-transform: uppercase;
    color: var(--white);
  }

  /* Front */
  .card-front { background: var(--white); }
  .card-front .waves { position: absolute; inset: 0; }
  .card-front .brand {
    position: absolute;
    right: 50px; top: 62px;
    text-align: right;
  }
  .card-front .brand-name { color: var(--navy); font-size: 34px; }
  .card-front .brand-dot { width: 30px; height: 30px; background: var(--navy); }
  .card-front .brand-tagline { color: var(--navy); font-size: 9.5px; margin-top: 8px; }

  .contact {
    position: absolute;
    right: 50px; top: 266px;
    text-align: right;
    color: var(--white);
  }
  .person-name {
    font-size: 22px;
    line-height: 27px;
    font-weight: 700;
    letter-spacing: 1px;
    text-transform: uppercase;
    color: var(--green);
  }
  .person-title { font-size: 16px; line-height: 20px; font-weight: 500; margin-top: 2px; }
  .contact-list { list-style: none; margin-top: 8px; font-size: 13.5px; line-height: 21px; }
  .contact-list li { display: flex; justify-content: flex-end; align-items: center; gap: 7px; }
  .icon { width: 13px; height: 13px; flex: none; }
</style>
</head>
<body>

  <section class="card card-back">
    <div class="brand">
      <div class="brand-row">
        <span class="brand-dot"></span>
        <span class="brand-name">Clearfield Venture Partners</span>
      </div>
      <p class="brand-tagline">Your guide to confidently buy or sell a local business today</p>
    </div>
  </section>

  <section class="card card-front">
    <svg class="waves" viewBox="0 0 720 410" width="720" height="410">
      <path d="M0,100 C80,150 200,180 330,190 C220,186 90,160 0,128 Z" fill="var(--navy)"/>
      <path d="M0,132 C110,178 260,196 400,194 C520,192 600,198 660,224 C600,212 520,208 400,210 C260,212 110,196 0,160 Z" fill="var(--green)"/>
      <path d="M0,170 C130,210 280,222 410,220 C540,218 640,226 720,250 L720,410 L0,410 Z" fill="var(--navy)"/>
    </svg>

    <div class="brand">
      <div class="brand-row">
        <span class="brand-dot"></span>
        <span class="brand-name">Clearfield Venture Partners</span>
      </div>
      <p class="brand-tagline">Your guide to confidently buy or sell a local business today</p>
    </div>

    <div class="contact">
      <h1 class="person-name">Gavin L. Whitmore, CAIA</h1>
      <p class="person-title">Business Advisor</p>
      <ul class="contact-list">
        <li>(718) 294-7716
          <svg class="icon" viewBox="0 0 16 16"><rect x="4" y="1" width="8" height="14" rx="1.5" fill="none" stroke="var(--green)" stroke-width="1.6"/></svg>
          (917) 382-5047
          <svg class="icon" viewBox="0 0 16 16"><path d="M4 1.5 L6.5 1.5 L7.5 5 L5.8 6.3 C6.6 8 8 9.4 9.7 10.2 L11 8.5 L14.5 9.5 L14.5 12 C14.5 13.4 13.4 14.5 12 14.5 C6.5 14.2 1.8 9.5 1.5 4 C1.5 2.6 2.6 1.5 4 1.5 Z" fill="var(--green)"/></svg>
        </li>
        <li>g.whitmore@clearfieldventurepartners.example
          <svg class="icon" viewBox="0 0 16 16"><rect x="1.5" y="3.5" width="13" height="9" fill="none" stroke="var(--green)" stroke-width="1.5"/><path d="M1.5 3.5 L8 9 L14.5 3.5" fill="none" stroke="var(--green)" stroke-width="1.5"/></svg>
        </li>
        <li>www.clearfieldventurepartners.example
          <svg class="icon" viewBox="0 0 16 16"><circle cx="8" cy="8" r="6.5" fill="none" stroke="var(--green)" stroke-width="1.5"/><ellipse cx="8" cy="8" rx="2.8" ry="6.5" fill="none" stroke="var(--green)" stroke-width="1.2"/><path d="M1.5 8 H14.5" stroke="var(--green)" stroke-width="1.2"/></svg>
        </li>
      </ul>
    </div>
  </section>

</body>
</html>
```